Styling of small website for mid-sized Engineering and Manufacturing company

We need the styling for a professional website for a company wich delivers: engineering, manufacturing, assembling, servicing and prototyping. (typically, they produce complex devices in limited series (1-100 pieces. The client comes with an idea and they translate it into design and device).
We have already made a wire-frame, but need a style (colors, fonts, H1, H2, paragraphs, margins, padding etc).
The style must :
- express profession attitude (world of engineering)
- have a fresh, modern look
- be sober (enough (white) space between the elements
The style must also be able to be used in a RWD. At this moment the logo (just letters) uses a green color (#4C6E33), but it isn't an obligation to use the exact same color (even not the 'green' color itself if you think another color is better for the site).
Target Market(s)
engineering and production
Industry/Entity Type
It Company
Coding
Coded - Design and coding required
Number of Pages Required
5+ page

```html
<!DOCTYPE html>
<html lang="en">
<head>
<meta charset="utf-8">
<title>Veldmark – Engineering Solutions</title>
<link rel="stylesheet" href="https://fonts.googleapis.com/css2?family=Open+Sans:wght@400;600;700;800&display=swap">
<style>
:root{
  --accent:#1bbfdd;
  --ink:#333538;
  --muted:#9a9a9a;
  --line:#e3e3e3;
  --bar:#ececec;
  --band:#f2f2f2;
  --footer:#4a4d4e;
  --footer-line:#64686a;
  --dark:#141516;
  --white:#ffffff;
}
*{box-sizing:border-box;margin:0;padding:0}
html,body{width:1200px;height:2546px;overflow:hidden}
body{position:relative;background:var(--white);font-family:"Open Sans",Arial,sans-serif;color:var(--ink)}
.abs{position:absolute}
.sc{font-variant:small-caps}

/* header */
.site-header{position:absolute;left:0;top:0;width:1200px;height:102px;background:var(--white)}
.brand{position:absolute;left:115px;top:34px;display:flex;align-items:center;gap:10px}
.brand-mark{display:block;width:18px;height:18px;background:var(--accent)}
.brand-name{color:var(--ink);font-weight:600;font-size:22px;line-height:1}
.main-nav a{position:absolute;top:31px;height:37px;line-height:37px;font-size:14px;color:#555;text-decoration:none;transform:translateX(-50%)}
.main-nav a.active{background:var(--accent);color:var(--white);width:94px;text-align:center}

/* hero */
.hero{position:absolute;left:0;top:102px;width:1200px;height:523px;
  background:linear-gradient(90deg,#3c3630 0%,#6b6256 22%,#8d8a86 48%,#7d7a77 55%,#5f564c 78%,#3e3933 100%)}
.hero-shade{position:absolute;inset:0;background:linear-gradient(180deg,rgba(0,0,0,.15),rgba(0,0,0,.3))}
.hero-copy{position:absolute;left:0;top:120px;width:1200px;text-align:center;color:var(--white);font-weight:700}
.hero-l1{font-size:38px;line-height:44px}
.hero-l1 .first{color:var(--accent)}
.hero-l2{font-size:62px;line-height:64px}
.hero-l3{font-size:40px;line-height:48px}
.hero-text{width:660px;margin:12px auto 0;font-weight:400;font-size:11px;line-height:18px}
.btn-light{position:absolute;left:543px;top:356px;width:112px;height:39px;background:var(--white);color:var(--ink);font-size:13px;font-weight:600;line-height:39px;text-align:center}
.dots{position:absolute;display:flex;gap:4px}
.dots span{width:10px;height:10px;border-radius:50%;border:1.5px solid var(--white)}
.dots span.on{background:var(--white)}

/* service cards */
.card{position:absolute;top:701px;width:222px;height:300px;border:1px solid var(--line);background:var(--white)}
.card-photo{height:124px;background:linear-gradient(135deg,#9fc3cf,#5f8696)}
.card-icon{position:absolute;left:80px;top:94px;width:60px;height:60px;border-radius:50%;background:var(--accent);border:4px solid var(--white);box-shadow:0 0 0 1px var(--line)}
.card-icon svg{position:absolute;left:16px;top:16px}
.card-title{position:absolute;top:158px;width:100%;text-align:center;font-weight:700;font-size:17px}
.card-text{position:absolute;left:16px;top:190px;width:188px;font-size:9px;line-height:15.5px;color:var(--muted);text-align:justify}
.more-bar{position:absolute;left:0;bottom:0;width:100%;height:29px;background:var(--bar)}
.more-bar span,.view-bar span{display:block;width:76px;height:29px;background:var(--accent);color:var(--white);font-size:9px;line-height:29px;text-align:center}

/* intro */
.intro-text{position:absolute;left:250px;top:1061px;width:700px;text-align:center;font-size:10px;line-height:18px;color:var(--muted)}
.divider{position:absolute;left:440px;top:1130px;width:320px;height:1px;background:var(--line)}
.divider-icon{position:absolute;left:575px;top:1105px;width:50px;height:50px;border-radius:50%;background:var(--accent);border:4px solid var(--white);box-shadow:0 0 0 1px var(--line)}
.welcome{position:absolute;left:0;top:1185px;width:1200px;text-align:center;font-size:68px;font-weight:800;line-height:80px}
.welcome-sub{position:absolute;left:0;top:1264px;width:1200px;text-align:center;font-size:11px;color:var(--ink)}
.welcome-sub b{color:var(--accent);font-size:16px}

/* columns */
.col-title{position:absolute;top:1335px;font-size:22px;font-weight:700}
.col-rule{position:absolute;top:1368px;height:1px;background:var(--line)}
.col-rule i{position:absolute;right:0;top:-3px;width:55px;height:4px;background:var(--accent)}
.case-photo{position:absolute;left:115px;top:1381px;width:192px;height:141px;background:radial-gradient(circle at 45% 45%,#4a7d90,#1b2a33 75%)}
.case-text{position:absolute;left:328px;width:246px;font-size:9px;line-height:15px;color:var(--muted)}
.view-bar{position:absolute;top:1554px;width:459px;height:29px;background:var(--bar)}
.reason{position:absolute;left:626px;width:457px;height:44px;border:1px solid var(--line);font-size:12px;font-weight:600;line-height:42px;padding-left:20px}
.reason .toggle{position:absolute;right:-1px;top:-1px;width:54px;height:44px;background:var(--accent)}
.reason .toggle svg{position:absolute;left:15px;top:10px}

/* testimonials */
.testimonials{position:absolute;left:0;top:1668px;width:1200px;height:380px;background:radial-gradient(ellipse at 50% 50%,#2a2c2e,var(--dark) 80%)}
.t-title{position:absolute;top:48px;width:100%;text-align:center;color:var(--white);font-size:21px;font-weight:700}
.t-rule{position:absolute;left:373px;top:96px;width:453px;height:1px;background:#777}
.t-rule i{position:absolute;left:200px;top:-2px;width:53px;height:4px;background:var(--accent)}
.avatar{position:absolute;left:551px;top:115px;width:98px;height:98px;border-radius:50%;border:4px solid var(--white);background:linear-gradient(160deg,#b99b86,#6d5548)}
.t-quote{position:absolute;left:260px;top:233px;width:680px;text-align:center;color:#d6d6d6;font-size:10px;line-height:18px}
.t-name{position:absolute;top:277px;width:100%;text-align:center;color:var(--white);font-weight:700;font-size:15px}
.t-role{position:absolute;top:303px;width:100%;text-align:center;color:#d6d6d6;font-size:11px}

/* partners */
.partners{position:absolute;left:0;top:2048px;width:1200px;height:107px;background:var(--band)}
.partner{position:absolute;top:38px;transform:translateX(-50%);display:flex;align-items:center;gap:8px;color:#8a8a8a;font-size:27px;font-weight:600;line-height:30px}
.partner i{display:block;width:28px;height:28px;border-radius:50%;background:#a8a8a8}

/* footer */
.site-footer{position:absolute;left:0;top:2155px;width:1200px;height:391px;background:var(--footer);color:#e9e9e9}
.f-head{position:absolute;top:67px;font-size:17px;font-weight:400;letter-spacing:.3px}
.f-head-rule{position:absolute;left:465px;top:100px;width:617px;height:1px;background:var(--footer-line)}
.f-links{position:absolute;top:127px;list-style:none;font-size:11px;line-height:19.5px}
.field{position:absolute;background:var(--white);color:#999;font-size:10px;padding:6px 6px}
.submit{position:absolute;left:485px;top:233px;width:392px;height:26px;background:var(--accent);color:var(--white);font-size:11px;font-weight:700;text-align:center;line-height:26px}
.loc{position:absolute;left:908px;font-size:11px;line-height:16px}
.loc svg{position:absolute;left:0;top:3px}
.loc p{margin-left:33px}
.f-bottom-rule{position:absolute;left:115px;top:280px;width:967px;height:1px;background:var(--footer-line)}
.copyright{position:absolute;left:115px;top:301px;font-size:9px;letter-spacing:1px;color:#b9b9b9}
.socials{position:absolute;right:118px;top:298px;display:flex;gap:12px;font-size:11px;font-weight:700;color:var(--white)}
</style>
</head>
<body>

<header class="site-header">
  <div class="brand">
    <i class="brand-mark"></i>
    <span class="brand-name">Veldmark</span>
  </div>
  <nav class="main-nav">
    <a class="active" href="#" style="left:578px">Home</a>
    <a href="#" style="left:671px">Service</a>
    <a href="#" style="left:757px">Portfolio</a>
    <a href="#" style="left:838px">News</a>
    <a href="#" style="left:932px">About ACME</a>
    <a href="#" style="left:1043px">Contact Us</a>
  </nav>
</header>

<section class="hero">
  <div class="hero-bg abs" role="img" aria-label="Upward view of city office buildings and a glass skyscraper" style="inset:0"></div>
  <div class="hero-shade"></div>
  <div class="hero-copy sc">
    <div class="hero-l1"><span class="first">T</span>echonological</div>
    <div class="hero-l2">Solutions</div>
    <div class="hero-l3">From Idea To Product</div>
    <p class="hero-text">Acme ontwerpt en fabriceert toestellen voor de meest uiteenlopende industrieën, metaals belangrijkste de paramedische sector. Onze oplossingen zijn even veelzijdig als de vragen van onze klanten. Engineering, prototype, (serie)productie en service onder één dak. Dat maakt het traject van vraag naar oplossing sneller en beter beheersbaar.</p>
  </div>
  <a class="btn-light sc">Read More</a>
  <div class="dots" style="left:580px;top:490px"><span></span><span class="on"></span><span></span></div>
</section>

<section class="services">
  <article class="card" style="left:115px">
    <div class="card-photo" role="img" aria-label="Mechanical gears and engineering parts"></div>
    <div class="card-icon"><svg width="20" height="20" viewBox="0 0 20 20"><circle cx="10" cy="10" r="6.5" fill="none" stroke="#fff" stroke-width="3" stroke-dasharray="3 2"/><circle cx="10" cy="10" r="2.5" fill="#fff"/></svg></div>
    <h3 class="card-title sc">Engineering</h3>
    <p class="card-text">Lorem ipsum dolor sit amet. Cras ultricies ligula sed magna dictum porta. Lorem ipsum dolor sit amet, consectetur adipiscing elit. Lorem ipsum dolor sit amet, consectetur</p>
    <div class="more-bar"><span>More Info</span></div>
  </article>
  <article class="card" style="left:363px">
    <div class="card-photo" role="img" aria-label="Hands working on an electronics prototype" style="background:linear-gradient(135deg,#8fa3ad,#4d5e66)"></div>
    <div class="card-icon"><svg width="20" height="20" viewBox="0 0 20 20"><rect x="5" y="5" width="10" height="10" fill="none" stroke="#fff" stroke-width="2"/><path d="M8 1v4M12 1v4M8 15v4M12 15v4M1 8h4M1 12h4M15 8h4M15 12h4" stroke="#fff" stroke-width="1.5"/></svg></div>
    <h3 class="card-title sc">Prototyping</h3>
    <p class="card-text">Lorem ipsum dolor sit amet. Cras ultricies ligula sed magna dictum porta. Lorem ipsum dolor sit amet, consectetur adipiscing elit. Lorem ipsum dolor sit amet, consectetur</p>
    <div class="more-bar"><span>More Info</span></div>
  </article>
  <article class="card" style="left:613px">
    <div class="card-photo" role="img" aria-label="Hands assembling a circuit board" style="background:linear-gradient(135deg,#a9c8d8,#5d8397)"></div>
    <div class="card-icon"><svg width="20" height="20" viewBox="0 0 20 20"><path d="M3 3h6v3a2 2 0 0 0 2 0V3h6v6h-3a2 2 0 0 0 0 2h3v6h-6v-3a2 2 0 0 0-2 0v3H3z" fill="#fff"/></svg></div>
    <h3 class="card-title sc">Assembleren</h3>
    <p class="card-text">Lorem ipsum dolor sit amet. Cras ultricies ligula sed magna dictum porta. Lorem ipsum dolor sit amet, consectetur adipiscing elit. Lorem ipsum dolor sit amet, consectetur</p>
    <div class="more-bar"><span>More Info</span></div>
  </article>
  <article class="card" style="left:860px">
    <div class="card-photo" role="img" aria-label="Servicing a green circuit board with a probe" style="background:linear-gradient(135deg,#6f9a6a,#2f4f3a)"></div>
    <div class="card-icon"><svg width="20" height="20" viewBox="0 0 20 20"><circle cx="10" cy="6" r="4" fill="#fff"/><path d="M3 19c0-5 3-7 7-7s7 2 7 7z" fill="#fff"/></svg></div>
    <h3 class="card-title sc">Servicing</h3>
    <p class="card-text">Lorem ipsum dolor sit amet. Cras ultricies ligula sed magna dictum porta. Lorem ipsum dolor sit amet, consectetur adipiscing elit. Lorem ipsum dolor sit amet, consectetur</p>
    <div class="more-bar"><span>More Info</span></div>
  </article>
</section>

<section class="intro">
  <p class="intro-text sc">Van het eerste idee tot het kant-en-klare apparaat, volledig in eigen huis worden ontwikkeld. Engineering, prototype, (serie)productie en service onder één dak. Dat maakt het traject van vraag naar oplossing sneller en beter beheersbaar.</p>
  <div class="divider"></div>
  <div class="divider-icon"><svg class="abs" style="left:12px;top:12px" width="18" height="18" viewBox="0 0 20 20"><circle cx="10" cy="10" r="6.5" fill="none" stroke="#fff" stroke-width="3" stroke-dasharray="3 2"/><circle cx="10" cy="10" r="2.5" fill="#fff"/></svg></div>
  <h1 class="welcome sc">Welcome!</h1>
  <p class="welcome-sub sc"><b>Veldmark</b> &nbsp;is an indipendent engineering company</p>
</section>

<section class="showcase">
  <h2 class="col-title sc" style="left:115px">Show case Client X</h2>
  <div class="col-rule" style="left:115px;width:459px"><i></i></div>
  <div class="case-photo" role="img" aria-label="Abstract technology visual for the client showcase"></div>
  <p class="case-text sc" style="top:1381px">Lorem ipsum dolor sit amet. Cras ultricies ligula sed magna dictum porta. Lorem ipsum dolor sit amet, consectetur adipiscing elit. Lorem ipsum dolor sit amet, consectetur adipiscing. Amet ipsum.</p>
  <p class="case-text sc" style="top:1456px">Lorem ipsum dolor sit amet. Cras ultricies ligula sed magna dictum porta. Lorem ipsum dolor sit amet, consectetur adipiscing elit. Lorem ipsum dolor sit amet, consectetur adipiscing. Amet ipsum.</p>
  <div class="view-bar" style="left:115px"><span>View Portfolio</span></div>

  <h2 class="col-title sc" style="left:626px">Waarom Klanten Voor Ons Kiezen</h2>
  <div class="col-rule" style="left:626px;width:457px"><i></i></div>
  <div class="reason sc" style="top:1391px">Al 4.251 abonnees<span class="toggle"><svg width="24" height="24" viewBox="0 0 24 24"><circle cx="12" cy="12" r="10" fill="none" stroke="#fff" stroke-width="2"/><path d="M7 10l5 5 5-5" fill="none" stroke="#fff" stroke-width="2"/></svg></span></div>
  <div class="reason sc" style="top:1438px">1 keer per maand<span class="toggle"><svg width="24" height="24" viewBox="0 0 24 24"><circle cx="12" cy="12" r="10" fill="none" stroke="#fff" stroke-width="2"/><path d="M7 10l5 5 5-5" fill="none" stroke="#fff" stroke-width="2"/></svg></span></div>
  <div class="reason sc" style="top:1485px">Exclusieve tips en promo's<span class="toggle"><svg width="24" height="24" viewBox="0 0 24 24"><circle cx="12" cy="12" r="10" fill="none" stroke="#fff" stroke-width="2"/><path d="M7 10l5 5 5-5" fill="none" stroke="#fff" stroke-width="2"/></svg></span></div>
  <div class="view-bar" style="left:626px;width:457px"><span>View Portfolio</span></div>
</section>

<section class="testimonials" role="img" aria-label="Dark background of machine gears behind the client quote">
  <h2 class="t-title sc">What clients say about us</h2>
  <div class="t-rule"><i></i></div>
  <div class="avatar" role="img" aria-label="Client portrait"></div>
  <p class="t-quote sc">Vestibulum ac diam sit amet quam vehicula elementum sed sit amet dui. Donec rutrum congue leo eget malesuada. Nulla quis lorem ut libero malesuada feugiat. Praesent sapien massa, convallis a pellentesque nec, egestas non nisi.</p>
  <div class="t-name sc">John Doe</div>
  <div class="t-role sc">CEO of DOE Enterprices</div>
  <div class="dots" style="left:580px;top:345px"><span></span><span class="on"></span><span></span></div>
</section>

<section class="partners">
  <div class="partner" style="left:226px"><i></i>Loopwise</div>
  <div class="partner" style="left:421px"><i></i>Corevant</div>
  <div class="partner" style="left:600px">Heronly</div>
  <div class="partner" style="left:778px">Sonarix</div>
  <div class="partner" style="left:969px">Tidemark</div>
</section>

<footer class="site-footer">
  <h4 class="f-head" style="left:115px">NAVIGATION</h4>
  <h4 class="f-head" style="left:282px">OTHER LINKS</h4>
  <h4 class="f-head" style="left:465px">CONTACT US</h4>
  <h4 class="f-head" style="left:908px">OUR LOCATION</h4>
  <div class="f-head-rule"></div>
  <ul class="f-links" style="left:128px"><li>Home</li><li>Service</li><li>Portfolio</li><li>News</li><li>About ACME</li><li>Contact Us</li></ul>
  <ul class="f-links" style="left:295px"><li>Forums</li><li>Promotions</li><li>Sitemap</li><li>Blog</li></ul>
  <div class="field" style="left:485px;top:122px;width:189px;height:26px">Name</div>
  <div class="field" style="left:485px;top:160px;width:189px;height:26px">E-mail</div>
  <div class="field" style="left:485px;top:197px;width:189px;height:26px">Phone</div>
  <div class="field" style="left:687px;top:122px;width:190px;height:100px">Message</div>
  <div class="submit">SUBMIT</div>
  <div class="loc" style="top:128px">
    <svg width="18" height="16" viewBox="0 0 18 16"><path d="M9 1L1 8h2.5v7h4v-5h3v5h4V8H17z" fill="#fff"/></svg>
    <p>2170 HARBOUR LANE,<br>EASTMOOR, KT 12 AB 34.</p>
  </div>
  <div class="loc" style="top:179px">
    <svg width="16" height="16" viewBox="0 0 16 16"><path d="M3 1l3 3-1.5 2.5c1 2 3 4 5 5L12 10l3 3-2 2.5C7 15 1 9 .8 3z" fill="#fff"/></svg>
    <p>TELEPHONE: +1 555 0142 77<br>FAX: +1 555 0142 78</p>
  </div>
  <div class="f-bottom-rule"></div>
  <p class="copyright">COPYRIGHT (C) VELDMARK 2015-2016</p>
  <div class="socials"><span>Linko</span><span>Pindle</span><span>Vidra</span><span>Folkly</span><span>Chirpo</span><span>Gplex</span></div>
</footer>

</body>
</html>
```